Implant Denture Brochure

I would like to make a brochure to advertise implant dentures. This is for my dental clinic. I would like there to be some info about different implant denture options and advertise general cost. I like to use blue as a color and white. I may want to add or remove info based on the layout. Images of dentures with implants but no real photos just drawings or educational images. Real images of people smiling with dentures.

Upper
1. Implants for Upper Denture Implant Supported Removable $10,000 - $12,000 ( Includes fee for extraction of remaining upper teeth, in office sedation fees, Implant placement and necessary surgery of at least 4 implants, Does not include denture)
2. Upper Denture Implant Supported Fixed Bridge (Zirconia) $25,000 (Includes fee for extraction of all upper teeth, in office sedation fee, Implant placement and necessary surgery of at least 4 implants, includes temporary denture, and final denture)

Lower
1. Implants for Removable Lower Denture Implant Retained $5,000 - $7,000 (Includes fee for extraction of remaining lower teeth, in office sedation fees, Implant placement and necessary surgery of at least 2 implants, Does not include denture)

2. Implants for Removable Lower Denture Implant Supported $10,000 - $12,000 (Includes fee for extraction of remaining lower teeth, in office sedation fees, Implant placement and necessary surgery of at least 4 implants, Does not include denture)

3. Lower Denture Implant Supported Fixed Bridge (Zirconia) $25,000 (Includes fee for extraction of all upper teeth, in office sedation fee, Implant placement and necessary surgery of at least 4 implants, includes temporary denture, and final denture)

Copper Brook Dental
#7 - 518 Larkspur Rd E.
Copper Brook, Alberta

```html
<!DOCTYPE html>
<html lang="en">
<head>
<meta charset="utf-8">
<title>Copper Brook Dental – Implant Denture</title>
<link href="https://fonts.googleapis.com/css2?family=Open+Sans:wght@400;600;700&display=swap" rel="stylesheet">
<style>
:root{
  --page-bg:#5d5f63;
  --white:#ffffff;
  --ink:#151515;
  --navy:#1f4a72;
  --blue:#2f7fc0;
  --sky:#4aa8e0;
  --cyan:#3fc0f0;
  --pale:#8fd3f5;
  --photo-a:#cfe3f2;
  --photo-b:#9db9d1;
  --circle:#eef1f4;
}
*{box-sizing:border-box;margin:0;padding:0}
html,body{width:1200px;height:1126px;overflow:hidden}
body{background:var(--page-bg);font-family:"Open Sans",sans-serif;position:relative}
.flyer{position:absolute;left:215px;top:18px;width:770px;height:1090px;overflow:hidden;background:var(--white)}
.flyer-bg{position:absolute;inset:0}
.hero-photo{position:absolute;left:300px;top:0;width:470px;height:470px;
  background:radial-gradient(circle at 55% 40%,var(--photo-a),var(--photo-b) 80%);
  border-bottom-left-radius:260px}
.brand{position:absolute;left:60px;top:205px;display:flex;align-items:center;gap:14px}
.brand-dot{width:38px;height:38px;border-radius:50%;background:var(--ink)}
.brand-name{font-weight:700;font-size:30px;line-height:1.05;color:var(--ink);text-transform:uppercase;letter-spacing:1px;width:260px}
.title-pill{position:absolute;left:70px;top:300px;padding:8px 34px;border-radius:24px;
  background:linear-gradient(90deg,var(--sky),var(--blue));color:var(--white);font-weight:700;font-size:24px;letter-spacing:.5px}
.group{position:absolute;left:55px;width:665px;border:3px solid var(--pale);border-radius:30px;padding:34px 26px 18px 125px}
.group.upper{top:512px;height:200px}
.group.lower{top:750px;height:250px}
.tab{position:absolute;top:-22px;left:40px;width:260px;height:38px;border-radius:20px;
  background:linear-gradient(90deg,var(--pale),var(--cyan));color:var(--white);font-weight:700;font-size:22px;padding:4px 0 0 90px}
.thumb{position:absolute;left:22px;width:66px;height:66px;border-radius:50%;
  background:radial-gradient(circle,var(--white),var(--circle) 70%);box-shadow:0 2px 6px rgba(0,0,0,.35)}
.item{font-size:12.5px;line-height:16px;color:var(--white);margin-bottom:12px}
.item-title{color:var(--cyan);font-weight:700}
.bullet{display:inline-block;width:11px;height:11px;border-radius:50%;background:var(--cyan);margin-right:5px;vertical-align:-1px}
.contact{position:absolute;left:410px;top:1008px;color:var(--white);font-size:13px;line-height:22px}
.contact .phone{font-size:16px}
.contact svg{vertical-align:-4px;margin-right:6px}
.website{position:absolute;left:40px;top:1050px;font-size:19px;color:var(--ink)}
.website b{font-weight:700}
</style>
</head>
<body>
<main class="flyer">
  <svg class="flyer-bg" width="770" height="1090" viewBox="0 0 770 1090" aria-hidden="true">
    <defs>
      <linearGradient id="deep" x1="0" y1="0" x2="0" y2="1">
        <stop offset="0" stop-color="#1f4a72"/>
        <stop offset="1" stop-color="#2f8ccf"/>
      </linearGradient>
    </defs>
    <path d="M420,0 C470,60 600,70 770,40 L770,0 Z" fill="#6cc6ef"/>
    <path d="M0,488 C260,500 560,440 770,318 L770,1090 L0,1090 Z" fill="#8fd3f5"/>
    <path d="M0,502 C260,514 560,456 770,336 L770,1090 L0,1090 Z" fill="url(#deep)"/>
    <path d="M0,1052 C120,1020 260,1005 400,1030 L400,1090 L0,1090 Z" fill="#8fd3f5"/>
    <path d="M0,1062 C120,1030 260,1015 400,1040 C470,1055 560,1090 560,1090 L0,1090 Z" fill="#ffffff"/>
  </svg>

  <div class="hero-photo" role="img" aria-label="Photo of a smiling senior couple embracing"></div>

  <div class="brand">
    <span class="brand-dot"></span>
    <span class="brand-name">Copper Brook Dental</span>
  </div>
  <div class="title-pill">IMPLANT DENTURE</div>

  <section class="group upper">
    <div class="tab">UPPER</div>
    <div class="thumb" role="img" aria-label="Illustration of an upper implant-supported removable denture" style="top:30px"></div>
    <div class="thumb" role="img" aria-label="Illustration of an upper implant-supported fixed bridge" style="top:112px"></div>
    <p class="item"><span class="bullet"></span><span class="item-title">Implants for Upper Denture Implant Supported Removable</span> $10,000 - $12,000 (Includes fee for extraction of remaining upper teeth, in office sedation fees, Implant placement and necessary surgery of at least 4 implants, Does not include denture)</p>
    <p class="item"><span class="bullet"></span><span class="item-title">Upper Denture Implant Supported Fixed Bridge (Zirconia)</span> $25,000 (Includes fee for extraction of all upper teeth, in office sedation fee, Implant placement and necessary surgery of at least 4 implants, includes temporary denture, and final denture)</p>
  </section>

  <section class="group lower">
    <div class="tab">LOWER</div>
    <div class="thumb" role="img" aria-label="Illustration of a lower implant-retained removable denture" style="top:28px"></div>
    <div class="thumb" role="img" aria-label="Illustration of a lower implant-supported removable denture" style="top:102px"></div>
    <div class="thumb" role="img" aria-label="Illustration of a lower implant-supported fixed bridge" style="top:176px"></div>
    <p class="item"><span class="bullet"></span><span class="item-title">Implants for Removable Lower Denture Implant Retained</span> $5,000 - $7,000 (Includes fee for extraction of remaining lower teeth, in office sedation fees, Implant placement and necessary surgery of at least 2 implants, Does not include denture)</p>
    <p class="item"><span class="bullet"></span><span class="item-title">Implants for Removable Lower Denture Implant Supported</span> $10,000 - $12,000 (Includes fee for extraction of remaining lower teeth, in office sedation fees, Implant placement and necessary surgery of at least 4 implants, Does not include denture)</p>
    <p class="item"><span class="bullet"></span><span class="item-title">Lower Denture Implant Supported Fixed Bridge (Zirconia)</span> $25,000 (Includes fee for extraction of all upper teeth, in office sedation fee, Implant placement and necessary surgery of at least 4 implants, includes temporary denture, and final denture)</p>
  </section>

  <address class="contact" style="font-style:normal">
    <div class="phone"><svg width="16" height="16" viewBox="0 0 16 16"><circle cx="8" cy="8" r="8" fill="#151515"/><path d="M5 4.5l1.6-.4.9 2-1 .8a5 5 0 002.6 2.6l.8-1 2 .9-.4 1.6c-3.5.2-6.7-3-6.5-6.5z" fill="#fff"/></svg>+1 403-555-0148</div>
    <div><svg width="16" height="16" viewBox="0 0 16 16"><circle cx="8" cy="8" r="8" fill="#151515"/><path d="M8 3.8l4 3.4h-1.2V11H5.2V7.2H4z" fill="#fff"/></svg>#7 - 518 Larkspur Rd E. Copper Brook, Alberta</div>
  </address>

  <p class="website">www.<b>copperbrookdental</b>.ca</p>
</main>
</body>
</html>
```